Business card for a Exhibition booth fabrication company

Hi. My company would like to change our corporate name card. We are an events and Exhibition stand builder company. We would like our corporate name card to resonate what we do. I need someone to create something unique that relates to the industry that I am in. The graphic designer should be creative to incorporate the elements of my industry and try to blend in well in the design of the card. Our aim is to ensure that we are unique and our card can look different from our competitors.
Updates

The decision maker was very busy and didnt had time to make this decision

Target Market(s)

Marketing and events manager from all companies

Contact Information for Business Card

The business card should have the following details:
Name
Job Title
Email
Website

Colors

Designer to choose colors to be used in the design.

Requirements
Must have
• The card must be look something that is relevant to the service that I am providing. My website is: www.velmora-buildworks.example
• You can see my website to get more information on what service that I am doing
Nice to have
• On the back of my card, I would like to have a globe image with the incorporation of my company logo. This is to indicate that my services can be done in any part of the world.

```html
<!DOCTYPE html>
<html lang="en">
<head>
<meta charset="utf-8">
<title>Velmora Buildworks – Business Card</title>
<link href="https://fonts.googleapis.com/css2?family=Open+Sans:wght@400;600&display=swap" rel="stylesheet">
<style>
  :root {
    --stage: #4a4a4a;
    --card-dark: #2e2e2f;
    --card-light: #f4f4f4;
    --accent: #e0181e;
    --text-light: #f2f2f2;
    --text-dark: #4d4d4d;
    --globe: #3a3a3b;
  }
  * { margin: 0; padding: 0; box-sizing: border-box; }
  html, body { width: 1200px; height: 1021px; overflow: hidden; }
  body {
    background: var(--stage);
    font-family: "Open Sans", Arial, sans-serif;
    position: relative;
  }
  .card {
    position: absolute;
    left: 180px;
    width: 840px;
    height: 480px;
    overflow: hidden;
    box-shadow: 0 10px 24px rgba(0,0,0,.45);
  }
  /* Back side */
  .card-back { top: 22px; background: var(--card-dark); }
  .card-back .globe {
    position: absolute;
    left: 90px; top: 170px;
    width: 660px; height: 660px;
    border-radius: 50%;
    background: radial-gradient(circle at 50% 30%, #3d3d3e 0%, var(--globe) 45%, #323233 100%);
  }
  .card-back .brand {
    position: absolute;
    top: 170px; left: 0; right: 0;
    text-align: center;
    color: var(--text-light);
    font-weight: 600;
    font-size: 34px;
    letter-spacing: 6px;
  }
  .card-back .services {
    position: absolute;
    top: 300px; left: 0; right: 0;
    text-align: center;
    color: var(--text-light);
    font-size: 19px;
  }
  .services .sep { color: var(--accent); margin: 0 10px; }

  /* Front side */
  .card-front { top: 520px; background: var(--card-dark); }
  .card-front .panel-light {
    position: absolute; left: 0; top: 0; bottom: 0;
    width: 340px;
    background: linear-gradient(180deg, #fff, var(--card-light));
  }
  .card-front .divider {
    position: absolute; left: 340px; top: 0; bottom: 0;
    width: 4px; background: var(--accent);
  }
  .card-front .pointer {
    position: absolute; left: 344px; top: 118px;
    width: 0; height: 0;
    border-top: 11px solid transparent;
    border-bottom: 11px solid transparent;
    border-left: 12px solid var(--accent);
  }
  .card-front .brand {
    position: absolute; left: 0; width: 340px; top: 210px;
    text-align: center;
    color: var(--text-dark);
    font-weight: 600;
    font-size: 21px;
    letter-spacing: 3px;
  }
  .contact { position: absolute; left: 400px; top: 108px; color: var(--text-light); }
  .contact .name { color: var(--accent); font-weight: 600; font-size: 28px; line-height: 1.1; }
  .contact .role { font-size: 21px; margin-bottom: 26px; }
  .contact .line { display: flex; align-items: center; font-size: 21px; line-height: 31px; }
  .contact .line svg { width: 18px; height: 18px; margin-right: 12px; flex: none; }
  .contact .place { margin-left: 28px; }
</style>
</head>
<body>
  <section class="card card-back">
    <div class="globe" role="img" aria-label="Faint world globe showing continents"></div>
    <div class="brand">VELMORA BUILDWORKS</div>
    <p class="services">Exhibition Booth Builders<span class="sep">|</span>Outdoor Booth Set Up<span class="sep">|</span>Interior Design</p>
  </section>

  <section class="card card-front">
    <div class="panel-light"></div>
    <div class="brand">VELMORA BUILDWORKS</div>
    <div class="divider"></div>
    <div class="pointer"></div>
    <div class="contact">
      <p class="name">Daniel Hartley</p>
      <p class="role">President</p>
      <p class="line">
        <svg viewBox="0 0 24 24"><path fill="#e0181e" d="M6.6 10.8a15.1 15.1 0 0 0 6.6 6.6l2.2-2.2c.3-.3.7-.4 1-.2 1.1.4 2.3.6 3.6.6.6 0 1 .4 1 1V20c0 .6-.4 1-1 1A17 17 0 0 1 3 4c0-.6.4-1 1-1h3.5c.6 0 1 .4 1 1 0 1.3.2 2.5.6 3.6.1.3 0 .7-.2 1z"/></svg>
        +65 91004821<span class="place">Singapore</span>
      </p>
      <p class="line">
        <svg viewBox="0 0 24 24"><path fill="#e0181e" d="M6.6 10.8a15.1 15.1 0 0 0 6.6 6.6l2.2-2.2c.3-.3.7-.4 1-.2 1.1.4 2.3.6 3.6.6.6 0 1 .4 1 1V20c0 .6-.4 1-1 1A17 17 0 0 1 3 4c0-.6.4-1 1-1h3.5c.6 0 1 .4 1 1 0 1.3.2 2.5.6 3.6.1.3 0 .7-.2 1z"/></svg>
        +974 70002468<span class="place">Qatar</span>
      </p>
      <p class="line">
        <svg viewBox="0 0 24 24"><rect x="2" y="5" width="20" height="14" fill="none" stroke="#e0181e" stroke-width="2"/><path d="M2 5l10 8 10-8" fill="none" stroke="#e0181e" stroke-width="2"/></svg>
        info@velmora-buildworks.example
      </p>
      <p class="line">
        <svg viewBox="0 0 24 24"><circle cx="12" cy="12" r="9.5" fill="none" stroke="#e0181e" stroke-width="2"/><path d="M2.5 12h19M12 2.5c-3 3-3 16 0 19M12 2.5c3 3 3 16 0 19" fill="none" stroke="#e0181e" stroke-width="1.6"/></svg>
        www.velmora-buildworks.example
      </p>
    </div>
  </section>
</body>
</html>
```